Activity List

We need a brochure designed for the Brackley House, which is a holiday villa in Sri Lanka. The brochure will be sent to travel agents and holiday travellers by email and also be printed and placed at the Brackley House. The brochure should be sophisticated yet indicate a sense of adventure.

```html
<!DOCTYPE html>
<html lang="en">
<head>
<meta charset="utf-8">
<title>Brackley House – Activity List</title>
<link rel="stylesheet" href="https://fonts.googleapis.com/css2?family=Mulish:ital,wght@0,400;0,700;1,400&family=Questrial&display=swap">
<style>
:root{
  --page:#ece9e4;
  --paper:#ffffff;
  --ink:#3b3b3b;
  --heading:#168c70;
  --title:#1ea0c0;
  --brand:#149a96;
  --rule:#6fb8a6;
  --sky-top:#3a86d2;
  --sky-light:#e3eef8;
  --forest:#3c6a2b;
  --forest-deep:#264f1a;
}
*{box-sizing:border-box;margin:0;padding:0}
html,body{width:822px;height:1200px;overflow:hidden}
body{background:var(--page);font-family:"Questrial",sans-serif;color:var(--ink);position:relative}
.spread{position:absolute;left:87px;width:670px;height:518px;background:var(--paper);overflow:hidden}
.spread--outer{top:66px}
.spread--inner{top:632px;background:linear-gradient(180deg,#8fb4dc 0%,#c7daee 100%)}
.panel{position:absolute;top:0;height:518px}
.block{position:absolute;left:13px;right:9px}
.body-text{font-size:8px;line-height:9.2px;text-align:justify}
.note{font-style:italic}
.heading{font-family:"Mulish",sans-serif;font-weight:700;color:var(--heading);font-size:11px;line-height:14px;padding-bottom:3px;border-bottom:1px solid var(--rule)}
.heading small{font-size:8.6px}
.heading--plain{border-bottom:0}
.photo{position:absolute;border-radius:8px}

/* outer spread */
.panel--intro{left:0;width:224px;background:var(--paper)}
.intro-photo{position:absolute;left:0;top:0;width:224px;height:146px;background:linear-gradient(180deg,#5f8a49 0%,#3f6a30 45%,#2c3a28 100%)}
.intro-caption{position:absolute;left:0;top:64px;width:224px;height:82px;background:rgba(25,30,25,.72);color:#f2f2f2;font-size:7.6px;line-height:10.9px;padding:10px 10px 0 11px}
.section-title{position:absolute;left:14px;top:163px;font-size:14px;font-weight:400;color:var(--title);font-family:"Questrial",sans-serif;white-space:nowrap}
.cover{position:absolute;left:224px;top:0;width:446px;height:518px;background:linear-gradient(180deg,var(--sky-top) 0%,#7fb0e2 18%,#c9def3 38%,var(--sky-light) 55%,#b7c7c4 62%,#6f8f63 72%,var(--forest) 84%,var(--forest-deep) 100%)}
.brand-name{font-family:"Questrial",sans-serif;color:var(--brand);letter-spacing:.14em;text-transform:uppercase;display:flex;align-items:center;gap:6px}
.brand-dot{width:8px;height:8px;border-radius:50%;background:var(--brand)}
.contact{position:absolute;left:0;width:223px;top:208px;text-align:center;color:#4a4a4a;font-size:9.4px;line-height:13.6px}
.contact .brand-name{justify-content:center;font-size:10px;margin-bottom:12px}
.cover-title{position:absolute;left:223px;width:226px;top:216px;text-align:center}
.cover-title .brand-name{justify-content:center;font-size:13.6px;margin-bottom:14px}
.tagline{color:var(--brand);font-size:17.6px;line-height:21.5px}
.website{position:absolute;right:54px;bottom:18px;color:#fff;font-family:"Mulish",sans-serif;font-weight:700;font-size:9.4px}

/* inner spread */
.panel--a{left:0;width:218px;background:linear-gradient(90deg,#fff 0%,#fff 92%,#eef3f9 100%)}
.panel--b{left:228px;width:213px;background:linear-gradient(90deg,#f4f7fb 0%,#fff 10%,#fff 92%,#eef3f9 100%)}
.panel--c{left:451px;width:211px;background:linear-gradient(90deg,#f4f7fb 0%,#fff 10%,#fff 100%)}
.panel--b .block,.panel--c .block{left:7px;right:9px}
</style>
</head>
<body>

<section class="spread spread--outer">
  <div class="panel panel--intro">
    <div class="intro-photo" role="img" aria-label="Veranda looking out onto green forested hillside"></div>
    <p class="intro-caption">The Brackley House is a gateway to many of the Central Hill region's attractions such as Kandy, Kitulgala and Adam's Peak. It is an ideal choice for guests who want to explore the tourist trail while enjoying forests, streams, tea bushes and spice trees that make up the lush beauty of the hills.</p>
    <h1 class="section-title">Activities at the Brackley House</h1>

    <div class="block" style="top:196px">
      <h2 class="heading">Learn About Coffee and Spice</h2>
    </div>
    <p class="block body-text" style="top:222px">Join us for a morning walk through our 10-acre property where we grow several different spices and Arabica coffee. We show you how the plants are cultivated, encourage you to try your hand at picking any spices that are ready for harvesting and give you a brief history of the ancient spice trade while we are at it. <span class="note">(Activity provided free of charge)</span></p>
    <div class="photo" style="left:18px;top:299px;width:191px;height:105px;background:radial-gradient(circle at 40% 50%,#3c5a22 0%,#6e9a3a 45%,#c9dca6 100%)" role="img" aria-label="Green peppercorns hanging from a vine among leaves"></div>

    <div class="block" style="top:418px">
      <h2 class="heading">From Leaf to Cup <small>(20 minute by foot)</small></h2>
    </div>
    <p class="block body-text" style="top:446px">Walk down to the neighbourhood tea factory for a lesson on how Sri Lanka's most famous export – tea – is processed. Watch how a batch of freshly packed tea leaves is transformed into the familiar brew that is enjoyed by millions around the world. <span class="note">(Activity provided free of charge based on availability)</span></p>
  </div>

  <div class="cover" role="img" aria-label="Blue sky with clouds above a misty, forested valley">
    <div class="contact">
      <div class="brand-name"><span class="brand-dot"></span>Brackley House</div>
      57/3 Mossgrove Lane,<br>Elmvale. Sri Lanka.<br>Tel: +94 - 81000 - 4217<br>Fax: +94 - 60000 - 4218<br>information@brackley-house.com
    </div>
    <div class="cover-title">
      <div class="brand-name">The Brackley House</div>
      <p class="tagline">A tranquility that<br>only nature bestows</p>
    </div>
    <div class="website">www.brackley-house.com</div>
  </div>
</section>

<section class="spread spread--inner">
  <div class="panel panel--a">
    <div class="block" style="top:17px"><h2 class="heading">The Kotmale Dam <small>(15 minutes)</small></h2></div>
    <p class="block body-text" style="top:44px">The impressive Kotmale Dam built in the 1980s is just a 15-minute drive from the Brackley. The Brackley House manager will accompany you to the dam and give you details on its construction. Take in the majesty of this engineering wonder and if the waters are low catch a glimpse of ancient temples that were submerged during its construction. If interested we will then take you to visit the Mahaweli Maha Seya a gigantic stupa built to replace the lost temples.</p>
    <p class="block body-text note" style="top:132px">($25 for a group up to 4 people using guest's vehicle, $50 per group in Brackley House vehicle)</p>
    <div class="photo" style="left:14px;top:157px;width:193px;height:95px;background:linear-gradient(90deg,#7a4a2a 0%,#c9a06a 30%,#d8b884 60%,#5f7a2e 100%)" role="img" aria-label="Chillies, limes and spices around a wooden chopping board"></div>
    <div class="block" style="top:266px"><h2 class="heading">Rice &amp; Spice Cookery Demonstration</h2></div>
    <p class="block body-text" style="top:293px">Spend a morning at the Brackley House with our cook Ruwan who will show you how to put together that lunch time staple of all Sri Lankan homes – the amazing rice and curry. He will give you tips, show you how to use spices, and even walk you through our gardens to collect produce for your meal. You then get to enjoy the meal you cooked and also receive the Brackley House Lunch, a booklet of rice and curry recipes.</p>
    <p class="block body-text note" style="top:378px">($25 per person)</p>
    <div class="block" style="top:403px"><h2 class="heading">Hill and Village Walk</h2></div>
    <p class="block body-text" style="top:431px">The Brackley House is located right across from a hill, that dominates our views. For those who like to explore on foot you can cross the stream at the bottom of our property and then walk through a shaded, meandering path that takes you past many village homes. For the more adventurous a steep climb will take you up to the top of the hill for fabulous views of the valley below.</p>
  </div>

  <div class="panel panel--b">
    <div class="block" style="top:17px"><h2 class="heading">Kitulgala <small>(1 hour)</small></h2></div>
    <p class="block body-text" style="top:45px">For adventure seekers – there's no better spot than Kitulgala. From white water rafting to canyoning, from kayaking to hiking, Kitulgala offers enough for a half-day or full day of activities.</p>
    <div class="block" style="top:95px"><h2 class="heading">Royal Botanical Gardens, Peradeniya (30 minutes)</h2></div>
    <p class="block body-text" style="top:141px">The Brackley House is located right across from a hill, that dominates our views. For those who like to explore on foot you can cross the stream at the bottom of our property and then walk through a shaded, meandering path that takes you past many village homes. For the more adventurous a steep climb will take you up to the top of the hill for fabulous views of the valley below.</p>
    <div class="photo" style="left:7px;top:218px;width:196px;height:94px;background:linear-gradient(180deg,#dfe6e6 0%,#7f8a74 40%,#4d6040 75%,#8aa070 100%)" role="img" aria-label="Avenue of tall palm trees in botanical gardens"></div>
    <div class="block" style="top:323px"><h2 class="heading heading--plain">Kandy (45 minutes)</h2></div>
    <p class="block body-text" style="top:353px">Kandy is famed for the Dalada Maligawa - the ancient royal palace that now houses the sacred tooth relic of the Lord Buddha. The Kandy Perahera, is held each year in August, and is a colourful spectacle of adorned elephants, fire dancers and traditional drummers.</p>
    <div class="photo" style="left:7px;top:412px;width:196px;height:96px;background:linear-gradient(180deg,#1f2c5a 0%,#2d3a70 40%,#d9a45a 70%,#7a4a22 100%)" role="img" aria-label="Illuminated temple building at night"></div>
  </div>

  <div class="panel panel--c">
    <div class="photo" style="left:11px;top:11px;width:190px;height:111px;background:linear-gradient(180deg,#2a4a9a 0%,#243f88 55%,#14224a 100%)" role="img" aria-label="Adam's Peak mountain silhouette against a blue dusk sky"></div>
    <div class="block" style="top:141px"><h2 class="heading">Adam's Peak <small>(45 minutes)</small></h2></div>
    <p class="block body-text" style="top:169px">Adam's Peak is a conspicuous, statuesque, triangular shape that announces its presence amidst its less well-proportioned mountain counterparts. The Peak is famous for its giant footprint, which is considered sacred by Buddhists, Hindus, Muslims and Christians alike. Climbing season commences in December and ends in May. The four-hour hike begins in the dead of night - in time to reach the summit to watch the first rays of sunlight pierce through the darkness to cast a perfect shadow of the mountain on the plains below.</p>
    <div class="block" style="top:284px"><h2 class="heading">The Temple Trio <small>(30 minutes)</small></h2></div>
    <p class="block body-text" style="top:313px">Step off the beaten track to visit three ancient temples built in the 14th century by kings who ruled the Gampola Kingdom. The three temples, Embekke, Gadaladeniya and Lankatilleka were regularly visited by both the kings and their wives. The temples are interesting, as despite their close proximity they differ considerably in their architecture.</p>
    <div class="block" style="top:394px"><h2 class="heading">Nuwara Eliya <small>(2.5 hours)</small></h2></div>
    <p class="block body-text" style="top:422px">Nuwara Eliya is fondly known as Little England - for its lovely Scottish style cottages and manicured gardens. For those who like a spot of golf while on holiday, Nuwara Eliya's golf course is considered one of the finest in Asia. The drive up to Nuwara Eliya from the Brackley House is spectacular as you meander past riverine forests, before breaking into the tea country - where hill-upon-hill is blanketed in brilliant green tea bushes.</p>
  </div>
</section>

</body>
</html>
```